She kept a summer stranger

She kept a summer stranger ", Author: Odile Marchand Size: 16 x 24 cm The publisher" Editions Parvel "should be placed on the bottom, with Gill without light Font The books is the portraits of women who had a lover younger or much younger than them

Target Market(s)

General Public

Colors

Designer to choose colors to be used in the design.

Requirements
Must have
• The 11 portraits

```html
<!DOCTYPE html>
<html lang="en">
<head>
<meta charset="utf-8">
<title>She kept a summer stranger — Odile Marchand</title>
<link href="https://fonts.googleapis.com/css2?family=Arimo:wght@700&family=Open+Sans:wght@600&family=Lato:wght@400&display=swap" rel="stylesheet">
<style>
  :root {
    --leather-light: #b0302b;
    --leather-mid: #962422;
    --leather-dark: #6e1716;
    --gilt: #c9a25a;
    --ink-white: #ffffff;
    --publisher-ink: #f3ece4;
  }
  html, body {
    margin: 0;
    padding: 0;
    width: 800px;
    height: 1200px;
    overflow: hidden;
    background: var(--leather-dark);
  }
  .cover {
    position: relative;
    width: 800px;
    height: 1200px;
    overflow: hidden;
    background:
      radial-gradient(ellipse at 45% 40%, var(--leather-light) 0%, var(--leather-mid) 55%, var(--leather-dark) 100%);
  }
  .gilt-frame {
    position: absolute;
    inset: 0;
  }
  .author {
    position: absolute;
    top: 72px;
    left: 0;
    width: 100%;
    margin: 0;
    text-align: center;
    font-family: "Open Sans", sans-serif;
    font-weight: 600;
    font-size: 25px;
    line-height: 34px;
    color: var(--ink-white);
    letter-spacing: 0.3px;
  }
  .title {
    position: absolute;
    top: 146px;
    left: 0;
    width: 100%;
    margin: 0;
    text-align: center;
    font-family: "Arimo", sans-serif;
    font-weight: 700;
    color: var(--ink-white);
    text-shadow: 0 2px 6px rgba(60, 0, 0, 0.45);
  }
  .title-main {
    display: block;
    font-size: 86px;
    line-height: 90px;
    letter-spacing: -0.5px;
  }
  .title-sub {
    display: block;
    font-size: 52px;
    line-height: 62px;
    letter-spacing: -0.3px;
  }
  .portrait-grid {
    position: absolute;
    left: 42px;
    top: 384px;
    width: 719px;
    height: 646px;
    display: grid;
    grid-template-columns: repeat(30, 1fr);
    grid-template-rows: 317px 329px;
    box-shadow: 0 3px 10px rgba(40, 0, 0, 0.4);
  }
  .portrait { display: block; }
  .portrait-grid .portrait:nth-child(-n+6) { grid-column: span 5; }
  .portrait-grid .portrait:nth-child(n+7) { grid-column: span 6; }
  .portrait--empress   { background: linear-gradient(160deg, #8d8a7a 0%, #e8d8be 55%, #a5322a 100%); }
  .portrait--silver    { background: linear-gradient(170deg, #d6d6d4 0%, #6f6f6f 60%, #3e3e3e 100%); }
  .portrait--smile     { background: linear-gradient(170deg, #3a3a3a 0%, #b9b9b9 50%, #d8d8d8 100%); }
  .portrait--scientist { background: linear-gradient(170deg, #2e2e2e 0%, #8a8a8a 45%, #1f1f1f 100%); }
  .portrait--writer    { background: linear-gradient(170deg, #5f4a3c 0%, #c9b2a2 50%, #9b4052 100%); }
  .portrait--actress   { background: linear-gradient(170deg, #4a3a34 0%, #c8a48c 50%, #6a2c2c 100%); }
  .portrait--novelist  { background: linear-gradient(170deg, #cfcac0 0%, #6e675e 55%, #4d463f 100%); }
  .portrait--singer    { background: linear-gradient(170deg, #2a1d18 0%, #a65a3c 40%, #d9b29c 70%, #141414 100%); }
  .portrait--elder     { background: linear-gradient(170deg, #1e1e1e 0%, #9a9a9a 50%, #cfcfcf 100%); }
  .portrait--crime     { background: linear-gradient(170deg, #6a5a58 0%, #dcc6bb 50%, #2d2a4a 100%); }
  .portrait--duchess   { background: linear-gradient(170deg, #4a2a20 0%, #e0c2a2 50%, #b8242a 100%); }
  .publisher {
    position: absolute;
    top: 1100px;
    left: 0;
    width: 100%;
    margin: 0;
    text-align: center;
    font-family: "Lato", sans-serif;
    font-weight: 400;
    font-size: 23px;
    line-height: 30px;
    color: var(--publisher-ink);
    letter-spacing: 0.4px;
  }
</style>
</head>
<body>
  <main class="cover">
    <svg class="gilt-frame" width="800" height="1200" viewBox="0 0 800 1200" aria-hidden="true">
      <rect x="12" y="12" width="776" height="1176" fill="none" stroke="var(--gilt)" stroke-width="1.5" opacity="0.8"/>
      <rect x="21" y="21" width="758" height="1158" fill="none" stroke="var(--gilt)" stroke-width="1" opacity="0.65"/>
    </svg>

    <p class="author">Odile Marchand</p>

    <h1 class="title">
      <span class="title-main">She kept a</span>
      <span class="title-sub">summer stranger</span>
    </h1>

    <section class="portrait-grid" aria-label="Portraits of the eleven women in the book">
      <div class="portrait portrait--empress" role="img" aria-label="Painted portrait of a woman in an empire-waist gown with a coral necklace"></div>
      <div class="portrait portrait--silver" role="img" aria-label="Black and white photograph of a dark-haired woman in a high-collared blouse"></div>
      <div class="portrait portrait--smile" role="img" aria-label="Black and white photograph of a smiling woman with a head wrap and necklace"></div>
      <div class="portrait portrait--scientist" role="img" aria-label="Black and white photograph of a woman in a dark dress with a pendant"></div>
      <div class="portrait portrait--writer" role="img" aria-label="Tinted photograph of a woman with curly hair and a pink scarf"></div>
      <div class="portrait portrait--actress" role="img" aria-label="Sepia photograph of a woman with wavy hair in a dark velvet dress"></div>
      <div class="portrait portrait--novelist" role="img" aria-label="Sepia photograph of a seated nineteenth-century woman in a striped cape"></div>
      <div class="portrait portrait--singer" role="img" aria-label="Colour photograph of a smiling woman with auburn hair and a cross pendant"></div>
      <div class="portrait portrait--elder" role="img" aria-label="Black and white close-up of an older woman wearing large glasses"></div>
      <div class="portrait portrait--crime" role="img" aria-label="Colourised portrait of an older woman with white hair and a brooch"></div>
      <div class="portrait portrait--duchess" role="img" aria-label="Renaissance painting of a red-haired woman with pearls and a jewel casket"></div>
    </section>

    <p class="publisher">Editions Parvel</p>
  </main>
</body>
</html>
```